Letterhead for invoices and engagement letter

Want to use logos sourced on quillorbit to create letterhead templates for word or pdf files

Industry/Entity Type

Legal- law firm

Colors
0054AA
0677BA
7BADD7
CADEEF
E8F1F8

```html
<!DOCTYPE html>
<html lang="en">
<head>
<meta charset="utf-8">
<title>The Harlow Firm – Letterhead</title>
<link href="https://fonts.googleapis.com/css2?family=Roboto:wght@400;500;700&family=Roboto+Condensed:wght@400;700&family=Great+Vibes&display=swap" rel="stylesheet">
<style>
  :root {
    --ink: #111111;
    --navy: #14213d;
    --bar: #000000;
    --paper: #ffffff;
  }
  * { margin: 0; padding: 0; box-sizing: border-box; }
  html, body { width: 941px; height: 1200px; overflow: hidden; background: var(--paper); }
  body { font-family: "Roboto", Arial, sans-serif; color: var(--ink); }
  .letterhead { position: relative; width: 941px; height: 1200px; }

  .side-bar { position: absolute; left: 89px; width: 25px; background: var(--bar); }
  .side-bar--top { top: 0; height: 34px; }
  .side-bar--bottom { top: 178px; bottom: 0; }

  .brand { position: absolute; left: 47px; top: 54px; display: flex; align-items: center; gap: 20px; }
  .brand-mark { width: 110px; height: 110px; border-radius: 50%; border: 4px solid var(--navy); background: var(--paper); flex: none; }
  .brand-name { font-size: 32px; line-height: 33px; font-weight: 400; color: var(--navy); letter-spacing: 1.5px; text-transform: uppercase; }

  .block { position: absolute; left: 144px; right: 93px; font-size: 16px; line-height: 20.5px; }
  .recipient { top: 218px; }
  .recipient-name { font-weight: 700; font-size: 18px; line-height: 22px; }
  .recipient-contact { margin-top: 10px; }
  .date { position: absolute; right: 93px; top: 218px; text-align: right; font-size: 16px; line-height: 20.5px; }
  .date-label { font-size: 18px; line-height: 22px; }

  .salutation { top: 388px; }
  .body-copy { top: 430px; text-align: justify; }
  .body-copy p + p { margin-top: 20.5px; }
  .closing { top: 758px; }

  .signature { position: absolute; left: 144px; top: 800px; font-family: "Great Vibes", cursive; font-size: 40px; line-height: 48px; color: var(--ink); }
  .signer { position: absolute; left: 144px; top: 862px; font-family: "Roboto Condensed", Arial, sans-serif; color: var(--navy); }
  .signer-name { font-weight: 700; font-size: 18px; line-height: 21px; }
  .signer-role { font-size: 16px; line-height: 19px; color: var(--ink); }

  .footer { position: absolute; left: 144px; top: 1063px; font-size: 16px; }
  .footer-line { display: flex; align-items: center; gap: 14px; height: 21.5px; }
  .footer-line svg { width: 16px; height: 16px; fill: var(--navy); flex: none; }
  .footer-address { margin-top: 10px; }
</style>
</head>
<body>
<main class="letterhead">
  <div class="side-bar side-bar--top"></div>
  <div class="side-bar side-bar--bottom"></div>

  <header class="brand">
    <div class="brand-mark"></div>
    <div class="brand-name">The<br>Harlow<br>Firm PLC</div>
  </header>

  <section class="block recipient">
    <div class="recipient-name">Name</div>
    <div>Owner</div>
    <div class="recipient-contact">
      000-000-0000<br>
      some @some.com<br>
      Some street, Some city<br>
      Some country
    </div>
  </section>

  <section class="date">
    <div class="date-label">Date</div>
    <div>31 December 2024</div>
  </section>

  <p class="block salutation">Dear Mr. Name</p>

  <section class="block body-copy">
    <p>Lorem ipsum dolor sit amet, consectetuer adipiscing elit, sed diam nonummy nibh euismod tincidunt ut laoreet dolore magna aliquam erat volutpat. Ut wisi enim ad minim veniam, quis nostrud exerci tation ullamcorper suscipit lobortis nisl ut aliquip ex ea commodo consequat. Duis autem vel eum iriure dolor in hendrerit in vulputate velit esse molestie.</p>
    <p>Lorem ipsum dolor sit amet, cons ectetuer adipiscing elit, sed diam nonummy nibh euismod tincidunt ut laoreet dolore magna aliquam erat volutpat. Ut wisi enim ad minim veniam, quis nostrud exerci tation ullamcorper suscipit lobortis nisl ut aliquip ex ea commodo consequat.</p>
    <p>Lorem ipsum dolor sit amet, consectetuer adipiscing elit, sed diam nonummy nibh euismod tincidunt ut laoreet dolore magna aliquam erat volutpat. Ut wisi enim ad minim veniam, quis nostrud exerci tation ullamcorper suscipit lobortis nisl ut aliquip ex ea commodo consequat.</p>
  </section>

  <p class="block closing">Thank you.</p>

  <div class="signature">Signature</div>
  <div class="signer">
    <div class="signer-name">Name</div>
    <div class="signer-role">Owner</div>
  </div>

  <footer class="footer">
    <div class="footer-line">
      <svg viewBox="0 0 24 24" aria-hidden="true"><path d="M6.6 10.8a15.1 15.1 0 0 0 6.6 6.6l2.2-2.2c.3-.3.7-.4 1-.2 1.1.4 2.3.6 3.6.6.6 0 1 .4 1 1V20c0 .6-.4 1-1 1A17 17 0 0 1 3 4c0-.6.4-1 1-1h3.5c.6 0 1 .4 1 1 0 1.3.2 2.5.6 3.6.1.3 0 .7-.2 1z"/></svg>
      <span>000-000-0030</span>
    </div>
    <div class="footer-line">
      <svg viewBox="0 0 24 24" aria-hidden="true"><path d="M2 5h20v14H2z M2 5l10 7 10-7" fill="none" stroke="#14213d" stroke-width="0"/><path d="M2 5h20v2l-10 6.5L2 7z M2 9l10 6.5L22 9v10H2z"/></svg>
      <span>info@theharlowfirm.com</span>
    </div>
    <div class="footer-line">
      <svg viewBox="0 0 24 24" aria-hidden="true"><circle cx="12" cy="12" r="9.5" fill="none" stroke="#14213d" stroke-width="1.6"/><ellipse cx="12" cy="12" rx="4" ry="9.5" fill="none" stroke="#14213d" stroke-width="1.4"/><path d="M2.5 12h19M4 7h16M4 17h16" stroke="#14213d" stroke-width="1.4"/></svg>
      <span>www.theharlowfirm.com</span>
    </div>
    <div class="footer-address">Address, Street, City, Country Zip code</div>
  </footer>
</main>
</body>
</html>
```